Business card design for engineering firm specializing in defense industry.

We need a professional business card design. Something simple but stands out. We are an engineering company specializing in composites in the defense industry.
Industry/Entity Type
Defense
Contact Information for Business Card
A simple black business card with the Varlonix yellow color is what we had in mind but open for other designs.
Colors
ffc214

```html
<!DOCTYPE html>
<html lang="en">
<head>
<meta charset="UTF-8">
<title>Varlonix Business Card</title>
<link href="https://fonts.googleapis.com/css2?family=Montserrat:wght@400;600;800&display=swap" rel="stylesheet">
<style>
  :root {
    --card-black: #1a1b1d;
    --brand-yellow: #ffc214;
    --text-white: #f4f4f4;
    --backdrop: #d9d9d9;
  }
  html, body {
    margin: 0;
    padding: 0;
    width: 1200px;
    height: 900px;
    overflow: hidden;
    background: var(--backdrop);
    font-family: "Montserrat", sans-serif;
  }
  .sheet {
    width: 1200px;
    height: 900px;
    display: flex;
    flex-direction: column;
    align-items: center;
    justify-content: center;
    gap: 56px;
  }
  .card {
    position: relative;
    width: 630px;
    height: 360px;
    background: var(--card-black);
    overflow: hidden;
    box-shadow: 0 10px 28px rgba(0,0,0,0.28);
  }
  /* Back side */
  .card-back {
    display: flex;
    align-items: center;
    justify-content: center;
  }
  .wordmark {
    display: flex;
    align-items: center;
    gap: 14px;
    color: var(--text-white);
    font-weight: 800;
    letter-spacing: 1px;
  }
  .wordmark-square {
    background: var(--brand-yellow);
  }
  .card-back .wordmark { font-size: 58px; }
  .card-back .wordmark-square { width: 34px; height: 34px; }

  /* Front side */
  .accent-panel {
    position: absolute;
    left: 0;
    top: 0;
    width: 220px;
    height: 100%;
    background: var(--brand-yellow);
  }
  .front-content {
    position: absolute;
    left: 268px;
    top: 44px;
    right: 30px;
  }
  .card-front .wordmark { font-size: 38px; }
  .card-front .wordmark-square { width: 22px; height: 22px; }
  .person-name {
    margin: 48px 0 0;
    color: var(--brand-yellow);
    font-weight: 600;
    font-size: 26px;
    letter-spacing: 1.5px;
  }
  .person-role {
    margin: 4px 0 0;
    color: var(--text-white);
    font-size: 15px;
  }
  .contact-list {
    list-style: none;
    margin: 30px 0 0;
    padding: 0;
  }
  .contact-item {
    display: flex;
    align-items: center;
    gap: 12px;
    color: var(--text-white);
    font-size: 15px;
    margin-bottom: 10px;
  }
  .contact-icon {
    width: 16px;
    height: 16px;
    flex: none;
  }
</style>
</head>
<body>
  <main class="sheet">
    <section class="card card-back" aria-label="Card back">
      <div class="wordmark">
        <span class="wordmark-square"></span>
        <span class="wordmark-name">Varlonix</span>
      </div>
    </section>

    <section class="card card-front" aria-label="Card front">
      <div class="accent-panel"></div>
      <div class="front-content">
        <div class="wordmark">
          <span class="wordmark-square"></span>
          <span class="wordmark-name">Varlonix</span>
        </div>
        <p class="person-name">MARA ELLISON</p>
        <p class="person-role">Director</p>
        <ul class="contact-list">
          <li class="contact-item">
            <svg class="contact-icon" viewBox="0 0 16 16" aria-hidden="true">
              <path d="M4 1.5 L6.2 4.5 L5 6 Q6.5 9.5 10 11 L11.5 9.8 L14.5 12 L13 14.5 Q5 14 1.5 3 Z" fill="var(--brand-yellow)"/>
            </svg>
            <span>555-014-2736</span>
          </li>
          <li class="contact-item">
            <svg class="contact-icon" viewBox="0 0 16 16" aria-hidden="true">
              <rect x="1" y="3" width="14" height="10" fill="var(--brand-yellow)"/>
              <path d="M1 3 L8 9 L15 3" fill="none" stroke="var(--card-black)" stroke-width="1.4"/>
            </svg>
            <span>mara.ellison@varlonix.com</span>
          </li>
          <li class="contact-item">
            <svg class="contact-icon" viewBox="0 0 16 16" aria-hidden="true">
              <circle cx="8" cy="8" r="7" fill="var(--brand-yellow)"/>
              <path d="M1 8 H15 M8 1 V15 M8 1 Q3 8 8 15 M8 1 Q13 8 8 15" fill="none" stroke="var(--card-black)" stroke-width="1"/>
            </svg>
            <span>www.varlonix.com</span>
          </li>
        </ul>
      </div>
    </section>
  </main>
</body>
</html>
```